Anzeigengestaltung für Brandschutzdienstleistungen und Schulungen
Zielgruppe
Wir sind ein Dienstleistungsunternehmen mit Schwerpunkt auf Planung, Betreuung und Schulung von Firmen im Bereich vorbeugenden betrieblichen und organisatorischen Brandschutz.
Aufgabenstellung
Wir hätten gerne ein Werbeflyer, vielleicht sogar als Zeitungseinlage, auf zwei Seiten bedruckt. Eine Seite mit Werbung zu unserer Schulungsangeboten Brandschutzhelfer und Erste Hilfe. Beides Anerkannt durch Berufsgenossenschaften. Kosten für Kurse der betriebliche Ersthelfer rechnen wir mit der BG ab und ist für Firmen teils kostenlos.
Bei den Schulungen folgende Hinweise. "Auch als Inhouse Schulung" und "auch online buchbar"
Zweite Seite das Angebot zur Betreuung der Firmen als Brandschutzberater bzw. externer Brandschutzbeauftragter.
Vorgaben aus unserer Homepage können gerne verwendet werden.

```html
<!DOCTYPE html>
<html lang="de">
<head>
<meta charset="utf-8">
<title>Brandschutz Wolters – Anzeige Seite 1</title>
<link href="https://fonts.googleapis.com/css2?family=Gelasio:wght@400&family=PT+Sans:wght@400;700&display=swap" rel="stylesheet">
<style>
  :root {
    --fire-red: #e3161b;
    --ink: #111111;
    --note-pink: #e0158a;
    --paper: #ffffff;
    --linen: #f2cdb8;
    --deep-red: #c8141a;
  }
  * { margin: 0; padding: 0; box-sizing: border-box; }
  html, body { width: 849px; height: 1200px; overflow: hidden; background: var(--paper); }
  .flyer {
    position: relative; width: 849px; height: 1200px; overflow: hidden;
    background: var(--paper); color: var(--ink);
    font-family: "PT Sans", sans-serif;
  }
  .draft-note {
    position: absolute; left: 706px; top: 18px;
    font-family: "Gelasio", serif; font-size: 15px; line-height: 20.5px;
    color: var(--note-pink);
  }
  .brand {
    position: absolute; left: 50px; top: 68px;
    display: flex; align-items: center; gap: 12px;
    font-family: "PT Sans", sans-serif; font-weight: 700; font-size: 32px;
    color: var(--fire-red);
  }
  .brand-square { width: 28px; height: 28px; background: var(--fire-red); }
  .hero-photo {
    position: absolute; left: 0; top: 192px; width: 849px; height: 400px;
    background: linear-gradient(90deg, var(--paper) 0%, var(--linen) 22%, #f7eee8 45%, #e9e4e2 58%, var(--deep-red) 80%, var(--fire-red) 100%);
  }
  .dash-rule { position: absolute; display: block; }
  .headline {
    position: absolute; left: 63px; top: 640px;
    font-family: "Gelasio", serif; font-weight: 400; font-size: 35px; line-height: 42px;
    white-space: nowrap;
  }
  .body-copy {
    position: absolute; left: 63px; top: 786px;
    font-size: 27.4px; line-height: 34px; white-space: nowrap;
  }
  .cta-box { position: absolute; left: 64px; top: 1005px; width: 382px; height: 152px; }
  .cta-box svg { position: absolute; inset: 0; }
  .cta-text {
    position: absolute; left: 33px; top: 22px;
    font-size: 27px; line-height: 34px; white-space: nowrap;
  }
  .contact { position: absolute; left: 468px; top: 1002px; font-size: 15.5px; font-style: normal; }
  .contact-name { font-weight: 700; font-size: 16px; margin-bottom: 18px; }
  .contact-list { display: grid; grid-template-columns: 90px auto; line-height: 20.5px; }
</style>
</head>
<body>
<main class="flyer">
  <div class="draft-note">Seite 1<br>Entwurf 001<br>Haldenberg</div>

  <div class="brand"><span class="brand-square"></span>Brandschutz Wolters</div>

  <div class="hero-photo" role="img" aria-label="Foto: aufgerollte Mullbinde links und roter Feuerlöscher mit Griff und Schlauch rechts"></div>

  <svg class="dash-rule" style="left:0;top:591px" width="849" height="8">
    <line x1="3" y1="4" x2="849" y2="4" stroke="var(--fire-red)" stroke-width="7" stroke-dasharray="15 20"/>
  </svg>

  <h1 class="headline">Wir alle wissen was diese Gegenstände sind…<br>Aber können wir sie auch richtig einsetzen?</h1>

  <svg class="dash-rule" style="left:63px;top:759px" width="786" height="8">
    <line x1="0" y1="4" x2="786" y2="4" stroke="var(--fire-red)" stroke-width="7" stroke-dasharray="15 19.6"/>
  </svg>

  <p class="body-copy">Bevor es zu spät ist, unterweisen Sie Ihre Mitarbeiter im<br>Brandschutz, denn laut Fachverband Technischer Brand-<br>schutz werden ca. 85&nbsp;% der Entstehungsbrände erfolgreich<br>mit einem Feuerlöscher bekämpft.</p>

  <div class="cta-box">
    <svg width="382" height="152" aria-hidden="true">
      <rect x="3.5" y="3.5" width="375" height="145" fill="none" stroke="var(--fire-red)" stroke-width="7" stroke-dasharray="15 19"/>
    </svg>
    <p class="cta-text">Kontaktieren Sie uns oder<br>melden Sie sich online bei<br>unseren Seminaren an!</p>
  </div>

  <address class="contact">
    <p class="contact-name">Brandschutz Wolters</p>
    <div class="contact-list">
      <span>Telefon</span><span>+49 (0)2403 7761230</span>
      <span>Email</span><span>info@brandschutz-wolters.de</span>
      <span>Homepage:</span><span>www.brandschutz-wolters.de</span>
      <span>Adresse</span><span>Lindenallee 7</span>
      <span></span><span>41063 Talheim</span>
    </div>
  </address>
</main>
</body>
</html>
```